Design a fresh new presentation folder for us!

We are looking for a fresh design of our new presentation folder.<br/><br/>We would like our current logo and colours being used in the design as well as images associated with our industry being international logistics.<br/><br/>Our services include, international freight - sea and air, domestic road transport, 3pl and warehousing.<br/><br/>We will attach our logo and other images we have used in the past to give you an idea of what we are after. Also attached our old folder.<br/><br/>We want a brand new fresh approach that is a really modern design. It needs to be visually striking.

Industry/Entity Type

Logistic

Colors
9ccb3b
acd037
cadf82
eef4d8

Requirements
Must have
• Fresh. Modern. Visually striking. Industry related.
• Slogan - Local Knowledge, Global Strength or Complete Logistics Solutions

```html
<!DOCTYPE html>
<html lang="en">
<head>
<meta charset="utf-8">
<title>Kestrel Freight Service – Presentation Folder</title>
<link href="https://fonts.googleapis.com/css2?family=Oswald:wght@300;500;600&family=Poppins:wght@400;500;600;700&display=swap" rel="stylesheet">
<style>
  :root{
    --green:#8cc63f;
    --green-bright:#9ccb3b;
    --green-light:#cadf82;
    --green-pale:#eef4d8;
    --green-deep:#4f8a1c;
    --grey:#6f6f6f;
    --grey-band:#6b6b6b;
    --paper:#f3f3f3;
    --backdrop:#dcdcdc;
    --ink:#222;
  }
  *{margin:0;padding:0;box-sizing:border-box}
  html,body{width:810px;height:1200px;overflow:hidden;background:var(--backdrop)}
  body{position:relative;font-family:"Poppins",sans-serif;color:var(--ink)}
  .label{position:absolute;font-family:"Poppins",sans-serif;font-size:16px;color:#111;letter-spacing:.2px}
  .label-front{left:178px;top:52px}
  .label-back{left:556px;top:52px}
  .label-inside{left:352px;top:1150px}

  .page{position:absolute;overflow:hidden;background:var(--paper)}
  .page::before,.page::after{content:"";position:absolute;left:0;right:0;height:10px;background:var(--grey-band);z-index:5}
  .page::before{top:0}.page::after{bottom:0}
  .page svg.art{position:absolute;inset:0;width:100%;height:100%}

  .front{left:57px;top:96px;width:333px;height:464px}
  .back{left:426px;top:96px;width:330px;height:464px;background:var(--green)}
  .spread-left{left:55px;top:600px;width:347px;height:520px}
  .spread-right{left:402px;top:600px;width:354px;height:520px}

  .brand{position:absolute;z-index:3;display:flex;align-items:center;gap:7px;font-family:"Poppins",sans-serif;font-weight:600;line-height:1.05;letter-spacing:1px;text-transform:uppercase}
  .brand .dot{width:14px;height:14px;border-radius:50%;background:currentColor;flex:none}
  .brand-green{color:var(--green)}
  .brand-white{color:#fff}

  .front .brand{left:172px;top:30px;font-size:11px}
  .web-pill{position:absolute;z-index:3;left:190px;top:83px;right:0;height:16px;background:var(--green);border-radius:8px 0 0 8px;color:#fff;font-size:7.5px;font-weight:600;letter-spacing:1px;white-space:nowrap;display:flex;align-items:center;padding-left:6px;gap:4px}
  .headline-band{position:absolute;left:0;top:207px;width:211px;height:57px;background:rgba(79,138,28,.85);z-index:2}
  .headline{position:absolute;left:19px;top:210px;z-index:3;font-family:"Oswald",sans-serif;font-weight:500;color:#fff;font-size:18px;line-height:24px;text-transform:uppercase;letter-spacing:-.3px;white-space:nowrap}
  .slogan{position:absolute;z-index:3;font-family:"Oswald",sans-serif;color:#fff;font-size:19px;line-height:24px;text-transform:uppercase;letter-spacing:-.2px;white-space:nowrap}
  .slogan .thin{font-weight:300}.slogan b{font-weight:600}
  .slogan-one{left:19px;top:330px}
  .slogan-two{left:70px;top:356px}

  .contact-title{position:absolute;left:20px;top:181px;font-weight:700;font-size:15px;color:#fff;letter-spacing:.3px;z-index:3}
  .contact-rule{position:absolute;left:190px;top:193px;width:122px;height:1px;background:#fff;z-index:3}
  .contact-band{position:absolute;left:0;right:0;top:206px;height:57px;background:rgba(79,138,28,.9);z-index:2}
  .contact-list{position:absolute;list-style:none;z-index:3;color:#fff;white-space:nowrap}
  .contact-list li{display:flex;align-items:center;gap:6px}
  .contact-list svg{flex:none;fill:#fff}
  .back .contact-list{left:20px;top:210px;font-size:6.5px;line-height:12.5px}
  .back .brand{left:184px;top:221px;font-size:8px}
  .back .brand .dot{width:11px;height:11px}

  .service-circle{position:absolute;left:125px;width:98px;height:98px;border-radius:50%;border:3px solid var(--green);padding:3px;background:#fff}
  .service-circle span{display:block;width:100%;height:100%;border-radius:50%}
  .c-sea{top:38px}.c-sea span{background:linear-gradient(170deg,#c9c4cf,#3a4660 55%,#6e5b52)}
  .c-air{top:174px}.c-air span{background:linear-gradient(180deg,#7d9192 45%,#e7e9ec 55%,#5a5a5a)}
  .c-road{top:311px}.c-road span{background:linear-gradient(180deg,#4f8fd6,#b9d6ef 40%,#b08a62 55%,#6e6e6a)}
  .flow-arrow{position:absolute;left:172px;width:4px;height:22px}
  .spread-left .brand{left:110px;top:463px;font-size:12px}
  .spread-right .brand{left:100px;top:340px;font-size:12px}
  .contact-card{position:absolute;left:36px;top:399px;width:283px;height:110px;background:var(--green-bright);border-radius:14px 14px 0 0}
  .spread-right .contact-list{left:66px;top:413px;font-size:11px;line-height:20px}
</style>
</head>
<body>
  <div class="label label-front">FRONT PAGE</div>
  <div class="label label-back">BACK PAGE</div>

  <section class="page front">
    <svg class="art" viewBox="0 0 333 464">
      <defs>
        <radialGradient id="globe" cx="30%" cy="40%" r="80%">
          <stop offset="0" stop-color="#a6d94a"/>
          <stop offset=".6" stop-color="#7cc043"/>
          <stop offset="1" stop-color="#4fa83a"/>
        </radialGradient>
      </defs>
      <path role="img" aria-label="Green world globe with continents" d="M0,11 L57,11 Q250,150 253,453 L0,453 Z" fill="url(#globe)"/>
      <path d="M160,118 Q244,250 243,453 L196,453 Q214,260 160,118 Z" fill="var(--grey)"/>
      <path d="M57,11 Q250,150 253,453 L247,453 Q244,160 57,11 Z" fill="var(--green-deep)"/>
    </svg>
    <div class="brand brand-green"><span class="dot"></span><span>Kestrel<br>Freight<br>Service</span></div>
    <div class="web-pill">
      <svg width="8" height="8" viewBox="0 0 10 10"><circle cx="5" cy="5" r="4.2" fill="none" stroke="#fff"/><path d="M1 5h8M5 1v8" stroke="#fff"/></svg>
      www.kestrelfreight.com
    </div>
    <div class="headline-band"></div>
    <h1 class="headline">A World of Experience<br>At Your Fingertips</h1>
    <p class="slogan slogan-one"><span class="thin">Local</span> <b>Knowledge,</b></p>
    <p class="slogan slogan-two"><span class="thin">Global</span> <b>Strength</b></p>
  </section>

  <section class="page back">
    <svg class="art" viewBox="0 0 330 464">
      <defs>
        <linearGradient id="backscene" x1="0" y1="0" x2="1" y2="1">
          <stop offset="0" stop-color="#8fc640"/>
          <stop offset=".5" stop-color="#82bd3c"/>
          <stop offset="1" stop-color="#6bbd52"/>
        </linearGradient>
      </defs>
      <rect role="img" aria-label="Faded cargo plane, globe and cruise ship over green" x="0" y="10" width="330" height="444" fill="url(#backscene)"/>
      <circle cx="290" cy="390" r="170" fill="#5fb64a" opacity=".45"/>
      <circle cx="320" cy="130" r="100" fill="#b5dc70" opacity=".45"/>
    </svg>
    <h2 class="contact-title">CONTACT WITH US</h2>
    <div class="contact-rule"></div>
    <div class="contact-band"></div>
    <ul class="contact-list">
      <li><svg width="6" height="7" viewBox="0 0 10 12"><path d="M5 0a4 4 0 0 0-4 4c0 3 4 8 4 8s4-5 4-8a4 4 0 0 0-4-4zm0 5.5a1.5 1.5 0 1 1 0-3 1.5 1.5 0 0 1 0 3z"/></svg>48 Harbour Way, Riverton, NSW 2190</li>
      <li><svg width="6" height="7" viewBox="0 0 8 12"><rect x="0.5" y="0.5" width="7" height="11" rx="1" fill="none" stroke="#fff"/></svg>+61 2 9000 1234</li>
      <li><svg width="6" height="7" viewBox="0 0 10 10"><rect x="0" y="3" width="10" height="7"/><rect x="2" y="0" width="6" height="3"/></svg>+61 2 9000 5678</li>
      <li><svg width="6" height="7" viewBox="0 0 10 10"><circle cx="5" cy="5" r="4.2" fill="none" stroke="#fff"/><path d="M1 5h8M5 1v8" stroke="#fff"/></svg>www.kestrelfreight.com</li>
    </ul>
    <div class="brand brand-white"><span class="dot"></span><span>Kestrel<br>Freight<br>Service</span></div>
  </section>

  <section class="page spread-left">
    <div class="service-circle c-sea"><span role="img" aria-label="Container ship at port"></span></div>
    <svg class="flow-arrow" style="top:142px" viewBox="0 0 4 22"><path d="M2 0v20M0 17l2 4 2-4" stroke="#555" fill="none"/></svg>
    <div class="service-circle c-air"><span role="img" aria-label="Passenger jet taking off"></span></div>
    <svg class="flow-arrow" style="top:279px" viewBox="0 0 4 22"><path d="M2 0v20M0 17l2 4 2-4" stroke="#555" fill="none"/></svg>
    <div class="service-circle c-road"><span role="img" aria-label="Open desert highway"></span></div>
    <div class="brand brand-green"><span class="dot"></span><span>Kestrel<br>Freight<br>Service</span></div>
  </section>

  <section class="page spread-right">
    <div class="brand brand-green"><span class="dot"></span><span>Kestrel<br>Freight<br>Service</span></div>
    <div class="contact-card"></div>
    <ul class="contact-list">
      <li><svg width="9" height="11" viewBox="0 0 10 12"><path d="M5 0a4 4 0 0 0-4 4c0 3 4 8 4 8s4-5 4-8a4 4 0 0 0-4-4zm0 5.5a1.5 1.5 0 1 1 0-3 1.5 1.5 0 0 1 0 3z"/></svg>48 Harbour Way, Riverton, NSW 2190</li>
      <li><svg width="9" height="11" viewBox="0 0 8 12"><rect x="0.5" y="0.5" width="7" height="11" rx="1" fill="none" stroke="#fff"/></svg>+61 2 9000 1234</li>
      <li><svg width="9" height="11" viewBox="0 0 10 10"><rect x="0" y="3" width="10" height="7"/><rect x="2" y="0" width="6" height="3"/></svg>+61 2 9000 5678</li>
      <li><svg width="9" height="11" viewBox="0 0 10 10"><circle cx="5" cy="5" r="4.2" fill="none" stroke="#fff"/><path d="M1 5h8M5 1v8" stroke="#fff"/></svg>www.kestrelfreight.com</li>
    </ul>
  </section>

  <div class="label label-inside">FOLDER INSIDE</div>
</body>
</html>
```